Compelling Home Page for Clip Harbor Partners

We are a Video SEO specialist that get websites on top of the front page of Zentrova and FlickBarn with video thumbprints that generate great traffic. Video SEO is all we do

see what we're offering at a salespage www.plumfieldreels.example. However, please omit "guarantee"

he home page should introduce our company as a premier company for helping brands get their videos on the front page of zentrova and high up in flickbarn. Should incorporate video "thumbnails" as part of the design. These could be the "triangular click buttons" or little video screens you see as "thumbnails" Needs a prominent place for a video about videoSEO. on Left side of page towards the top.

Needs buttons across the top for other pages. See www.brastonclips.example for frame of reference we want to be better than them.

Must incorporate our logo. We'd like to see the logo on dark background as well as white background.

Simple but with bright and vibrant highlights that look sophisticated, cutting edge and accountable. Shows credentials. Links with examples of thumbnails that are on the front page

We want to beat www.brastonclips.example check it out for point of reference

Target Market(s)

large corporations who have videos already and want to get better traction. Marlow 500. Advertising Agencies for Marlow 500's

Requirements
Must have
• Incorporate our logo. clean, easy to read

```html
<!DOCTYPE html>
<html lang="en">
<head>
<meta charset="utf-8">
<title>Clip Harbor Partners – Home</title>
<link rel="stylesheet" href="https://fonts.googleapis.com/css2?family=Arimo:wght@400;700&family=Roboto+Condensed:wght@700&display=swap">
<style>
:root{
  --header-top:#5a5a5a;
  --header-bottom:#000;
  --blue-deep:#0b2fc8;
  --blue-mid:#1d5ef0;
  --blue-light:#2f8cff;
  --gold:#ffcc00;
  --ink:#222;
  --heading:#555;
  --link:#1450d8;
  --title-blue:#17307a;
  --orange:#e8520c;
  --line:#e2e2e2;
}
*{box-sizing:border-box;margin:0;padding:0}
html,body{width:1200px;height:1055px;overflow:hidden;background:#fff}
body{position:relative;font-family:"Arimo",Arial,sans-serif;color:var(--ink)}
.abs{position:absolute}

/* header */
.site-header{left:0;top:0;width:1200px;height:125px;background:linear-gradient(#666 0%,#3c3c3c 50%,#050505 51%,#000 100%)}
.brand-box{left:36px;top:0;width:382px;height:123px;background:linear-gradient(#4a4a4a,#0c0c0c 55%,#1a1a1a);border:1px solid #555;border-top:none;display:flex;align-items:center;padding-left:10px;gap:10px}
.brand-dot{width:52px;height:52px;border-radius:50%;background:#f3a000;flex:none}
.brand-name{font-size:29px;font-weight:700;color:#fff;letter-spacing:-.5px;white-space:nowrap}
.main-nav{left:654px;top:40px;display:flex;align-items:center;height:48px}
.main-nav a{color:#fff;text-decoration:none;font-size:14px;position:absolute;top:16px;white-space:nowrap}
.main-nav a.active{top:0;left:0;width:82px;height:48px;line-height:48px;text-align:center;border-radius:9px;background:linear-gradient(#2aa0ff,#0a5ee0)}

/* banner */
.hero{left:0;top:125px;width:1200px;height:289px;background:radial-gradient(ellipse at 75% 10%,var(--blue-light),transparent 60%),linear-gradient(100deg,var(--blue-deep),var(--blue-mid) 60%,#1c7cf5);box-shadow:0 3px 5px rgba(0,0,0,.45)}
.video-panel{left:39px;top:14px;width:463px;height:224px;background:linear-gradient(#fff 40%,#cfcfcf);border:1px solid #ccc;border-radius:10px}
.panel-reflection{left:39px;top:242px;width:463px;height:42px;border-radius:10px 10px 0 0;background:linear-gradient(rgba(120,170,255,.55),rgba(30,80,230,0))}
.video-panel h2{position:absolute;left:24px;top:15px;font-weight:400;font-size:27px;color:var(--title-blue)}
.thumb{position:absolute;top:70px;width:99px;height:76px;border:2px solid #111;background:#fff;padding:2px}
.thumb-screen{width:100%;height:100%;background:linear-gradient(135deg,#2a1418,#5a2a30 50%,#c98c3a);position:relative}
.thumb-play{position:absolute;right:3px;bottom:3px;width:22px;height:20px;background:#d8d8e8;border:1px solid #888}
.thumb-play::after{content:"";position:absolute;left:7px;top:4px;border-left:9px solid #1a2a9a;border-top:6px solid transparent;border-bottom:6px solid transparent}
.arrow{position:absolute;top:100px}
.pager-btn{position:absolute;top:166px;width:97px;height:31px;border-radius:9px;background:linear-gradient(#ff7a2a,var(--orange) 50%,#c83e04);color:#fff;font-size:14px;line-height:31px;text-align:center;border:1px solid #b33a05}
.pager-btn span{position:absolute;top:0;width:16px;height:29px;background:linear-gradient(#ffb27a,#f08a50);color:#333;font-size:11px}
.hero-art{left:621px;top:39px;width:135px;height:129px;border-radius:50%;background:radial-gradient(circle at 40% 40%,#e6eefc,#7f9fcf 55%,rgba(60,90,180,0) 72%)}
.hero-headline{right:40px;top:18px;text-align:right;font-family:"Roboto Condensed",Arial,sans-serif;font-weight:700;font-size:35px;line-height:42px;color:#fff;text-shadow:1px 2px 3px rgba(0,0,40,.5)}
.hero-headline em{font-style:normal;color:var(--gold)}
.hero-sub{right:41px;top:238px;text-align:right;font-size:14px;line-height:17px;color:#fff}

/* content */
.rule{left:40px;top:434px;width:1158px;height:3px;background:var(--line)}
.intro{left:40px;top:456px;width:790px}
.intro h1{font-weight:400;font-size:25px;color:var(--heading);margin-bottom:12px}
.intro p{font-size:13.6px;line-height:23.4px;margin-bottom:23px}
.col-divider{left:845px;top:443px;width:4px;height:559px;background:#e8e8e8}
.side-card{left:870px;width:288px;background:#fff;border:1px solid #ddd;border-radius:9px;box-shadow:0 0 4px rgba(0,0,0,.18)}
.side-card h3{font-weight:400;font-size:26px;color:#333;padding:24px 0 0 17px;height:76px;border-bottom:3px solid #eee;margin:0 6px}
.card-icon{position:absolute;right:10px;top:14px}
.post{padding:0 0 0 38px;position:relative;font-size:12.5px;line-height:15px}
.post::before{content:"»";position:absolute;left:20px;top:0;color:#999}
.post a{color:var(--link);text-decoration:none}
.post-title{font-size:14px;display:block;margin-bottom:9px}
.post p{margin-bottom:11px}
.post-meta{font-size:12.5px;color:#555}
.post-meta .bubble{display:inline-block;vertical-align:-2px;margin-right:5px}
.quote{padding-left:38px;position:relative;font-size:12.5px;margin-bottom:15px}
.quote::before{content:"»";position:absolute;left:24px;color:#999}
.quote cite{display:block;text-align:right;padding-right:88px;font-style:italic;margin-top:6px}
.quote-art{position:absolute;right:18px;top:10px;width:56px;height:56px;background:linear-gradient(#fafafa,#d9d9d9);border:1px solid #ccc}
.read-more{display:block;text-align:right;padding-right:14px;color:var(--link);text-decoration:none;font-size:12.5px}

/* footer */
.footer-rule{left:0;top:1010px;width:1200px;height:3px;background:var(--line)}
.site-footer{left:0;top:1019px;width:1200px;height:36px;background:linear-gradient(#2d7af2,#1048d0);color:#fff;font-size:12.5px;text-align:center;line-height:36px}
</style>
</head>
<body>

<header class="abs site-header">
  <div class="abs brand-box"><span class="brand-dot"></span><span class="brand-name">Clip Harbor Partners</span></div>
  <nav class="abs main-nav">
    <a class="active" href="#">Home</a>
    <a href="#" style="left:96px">About Us</a>
    <a href="#" style="left:190px">Services</a>
    <a href="#" style="left:266px">Blog</a>
    <a href="#" style="left:330px">Portfolio</a>
    <a href="#" style="left:418px">Contact Us</a>
  </nav>
</header>

<section class="abs hero">
  <div class="abs video-panel">
    <h2>Video Listings</h2>
    <svg class="arrow" style="left:4px" width="14" height="16" viewBox="0 0 14 16"><path d="M12 1 3 8l9 7" fill="none" stroke="#000" stroke-width="3"/></svg>
    <div class="thumb" style="left:24px"><div class="thumb-screen" role="img" aria-label="Video thumbnail still"><span class="thumb-play"></span></div></div>
    <div class="thumb" style="left:129px"><div class="thumb-screen" role="img" aria-label="Video thumbnail still"><span class="thumb-play"></span></div></div>
    <div class="thumb" style="left:234px"><div class="thumb-screen" role="img" aria-label="Video thumbnail still"><span class="thumb-play"></span></div></div>
    <div class="thumb" style="left:339px"><div class="thumb-screen" role="img" aria-label="Video thumbnail still"><span class="thumb-play"></span></div></div>
    <svg class="arrow" style="left:443px" width="14" height="16" viewBox="0 0 14 16"><path d="M2 1l9 7-9 7" fill="none" stroke="#000" stroke-width="3"/></svg>
    <a class="pager-btn" style="left:24px"><span style="left:0;border-radius:8px 0 0 8px">‹</span>Prev</a>
    <a class="pager-btn" style="left:126px"><span style="right:0;border-radius:0 8px 8px 0">›</span>Next</a>
  </div>
  <div class="abs panel-reflection"></div>
  <div class="abs hero-art" role="img" aria-label="Chrome magnifying glass search illustration"></div>
  <p class="abs hero-headline">"FIRST PAGE <em>VIDEO LISTINGS</em><br>on Zentrova for the Keywords<br>of Your Choice...For More<br><em>Traffic</em>, Leads, and Sales to<br>Your Site!"</p>
  <p class="abs hero-sub">No matter what you sell or what your company size, VIDEO MARKETING is<br>very likely your best opportunity to&nbsp; dramatically increase online sales this year.</p>
</section>

<div class="abs rule"></div>

<main class="abs intro">
  <h1>Welcome to Clip Harbor Partners</h1>
  <p>Lorem Ipsum is simply dummy text of the printing and typesetting industry. Lorem Ipsum has been the industry's standard dummy text ever since the 1500s, when an unknown printer took a galley of type and scrambled it to make a type specimen book. It has survived not only five centuries, but also the leap into electronic typesetting, remaining essentially unchanged. It was popularised in the 1960s with the release of Typeflow sheets containing Lorem Ipsum passages, and more recently with desktop publishing software like Pagewright Studio including versions of Lorem Ipsum.</p>
  <p>Lorem Ipsum is simply dummy text of the printing and typesetting industry. Lorem Ipsum has been the industry's standard dummy text ever since the 1500s, when an unknown printer took a galley of type and scrambled it to make a type specimen book. It has survived not only five centuries, but also the leap into electronic typesetting, remaining essentially unchanged. It was popularised in the 1960s with the release of Typeflow sheets containing Lorem Ipsum passages, and more recently with desktop publishing software like Pagewright Studio including versions of Lorem Ipsum.</p>
</main>

<div class="abs col-divider"></div>

<aside class="abs side-card" style="top:454px;height:308px">
  <h3>Recent Blog item</h3>
  <svg class="card-icon" width="52" height="52" viewBox="0 0 52 52"><ellipse cx="26" cy="22" rx="24" ry="19" fill="#4ab8ec" stroke="#1e8cc8" stroke-width="2"/><path d="M14 38l-4 12 14-9z" fill="#4ab8ec"/><path d="M12 16h28M12 23h28M12 30h22" stroke="#fff" stroke-width="3"/></svg>
  <div class="post" style="margin-top:18px">
    <a class="post-title" href="#">Why Lorem ipsum dolor?</a>
    <p>Lorem Ipsum is simply dummy text of the printing and typesetting industry.</p>
    <div class="post-meta"><svg class="bubble" width="16" height="13" viewBox="0 0 16 13"><path d="M2 1h12v8H7l-4 3V9H2z" fill="none" stroke="#888"/></svg><a href="#">Comments 0</a> &nbsp;|&nbsp; <a href="#">Read More</a></div>
  </div>
  <div class="post" style="margin-top:24px">
    <a class="post-title" href="#">Why Lorem ipsum dolor?</a>
    <p>Lorem Ipsum is simply dummy text of the printing and typesetting industry.</p>
    <div class="post-meta"><svg class="bubble" width="16" height="13" viewBox="0 0 16 13"><path d="M2 1h12v8H7l-4 3V9H2z" fill="none" stroke="#888"/></svg><a href="#">Comments 0</a> &nbsp;|&nbsp; <a href="#">Read More</a></div>
  </div>
</aside>

<aside class="abs side-card" style="top:782px;height:214px">
  <h3>Testimonials</h3>
  <div class="quote-art" role="img" aria-label="Note paper with pencil illustration"></div>
  <div class="quote" style="margin-top:18px">Good Work - lorem ipsum / 1<cite>Dorian Vale</cite></div>
  <div class="quote">Good Work - lorem ipsum / 1<cite>Dorian Vale</cite></div>
  <a class="read-more" href="#">Read More</a>
</aside>

<div class="abs footer-rule"></div>
<footer class="abs site-footer">© 2011 Copyright : All Rights Reserved by Clip Harbor Partners</footer>

</body>
</html>
```